website in progress for new building development

Hi,
I have a new real estate development website in making but am running out of time for its completion. It's for a new apartment building for sales. Would it be possible for you to change/alter the site according to my requirements? I could send you all the existing files. The bulk of the website is done.
The images aren't really ready yet but will be within the next days so those will need to be replaced. Currently draft images are the placeholder on the website.

Let me know if you would be interested so we can quickly pick up correspondence.

This is the website so far (using Wordpress):
http://velmora.com.au/velmora/

Our domain is:
velmora.com.au

I am also adding the theme I am using.

Thanks.

Target Market(s)

Potential buyers.

Industry/Entity Type

Real Estate Development

Number of Pages Required

5+ page

Font styles to use
Other font styles liked:
• I used Robot under google fonts for the headlines

Requirements
Must have
• This is the current website
• http://velmora.com.au/velmora
• I'd like the colour scheme to remain the way it is.
• 1. Header
• I would like the header to have the menu on the right and have the 'Reigster' button similar to this website: (see the header here which shows up once you scroll down in the page) http://tesslinbyharvoquarter.com.au/
• Please adjust this feature into our website with the menu items given.
• 2. Logo on Homepage
• Add the velmora logo into the top center of the feature image.
• Though permanent images are yet to arrive in the next few days. These are only drafts.
• 3. Footer
• Not sure about the colour scheme here yet.
• Should contain Disclaimer and copyrights.
• 4.Pages:
• a) Home
• b) Building
• c) Interior
• d) Location
• e) Register
• 5. page 'Home'
• When you scroll down in velmora.com.au/velmora/ you see the three images under the feature image, I would like those being hyperlinked as a 'box' just like this website has them when you scroll down here:
• http://www.quilmadorne.com.au/
• 6. page 'Register'
• I like the subtle colour scheme for the form used here http://tesslinbyharvoquarter.com.au/#enquire-now
• and their 'Submit' button. Maybe adjust it to my website and remove the borders in the fields.
• 7. page 'Building'
• Will have two images of the exterior of the building which should be sliding automatically. (Images will be provided soon. For now I am only attaching draft images.)
• 8. page 'Interior'
• Will also have two images of the interior which should be automatically sliding. (Images will be provided soon. Attaching draft images for now)
Nice to have
• A language selection in the top right corner of each page:
• selection between english, mandarin, cantonese, korean.

```html
<!DOCTYPE html>
<html lang="en">
<head>
<meta charset="utf-8">
<title>Velmora – Interior</title>
<link rel="stylesheet" href="https://fonts.googleapis.com/css2?family=Roboto:wght@500;700&family=Open+Sans:wght@400&display=swap">
<style>
  :root {
    --header-bg: #030303;
    --page-bg: #eeedee;
    --card-bg: #f7f7f7;
    --card-border: #e4e4e4;
    --gold: #a8844b;
    --gold-light: #c9a063;
    --heading: #3a3a3a;
    --body-text: #7a7a7a;
    --chevron: #8a8a8a;
    --footer-bg: #333333;
    --white: #ffffff;
  }
  * { box-sizing: border-box; margin: 0; padding: 0; }
  html, body {
    width: 1200px; height: 764px; overflow: hidden;
    background: var(--page-bg);
    font-family: "Open Sans", Arial, sans-serif;
  }
  .page { position: relative; width: 1200px; height: 764px; }

  /* Header */
  .site-header {
    position: absolute; left: 0; top: 0; width: 1200px; height: 107px;
    background: var(--header-bg);
    border-bottom: 1px solid #c9c9c9;
  }
  .brand {
    position: absolute; left: 99px; top: 40px;
    font-family: "Roboto", Arial, sans-serif; font-weight: 500;
    font-size: 17px; letter-spacing: 6px; color: var(--gold-light);
    text-transform: uppercase;
  }
  .main-nav {
    position: absolute; left: 479px; top: 44px;
    display: flex; gap: 32px;
  }
  .main-nav a {
    font-family: "Roboto", Arial, sans-serif; font-weight: 500;
    font-size: 14.5px; letter-spacing: 1.2px; color: var(--white);
    text-decoration: none; text-transform: uppercase;
  }
  .register-btn {
    position: absolute; left: 890px; top: 35px; width: 126px; height: 40px;
    background: var(--gold); color: var(--white); border-radius: 2px;
    font-family: "Roboto", Arial, sans-serif; font-weight: 700;
    font-size: 14.5px; letter-spacing: 1.2px; text-decoration: none;
    display: flex; align-items: center; justify-content: center;
  }
  .lang-select {
    position: absolute; left: 1034px; top: 35px; width: 68px; height: 39px;
    border: 1px solid #bdbdbd; border-radius: 3px;
    display: flex; align-items: center; padding-left: 10px; gap: 10px;
  }

  /* Interior section */
  .section-title {
    position: absolute; left: 0; top: 160px; width: 1200px;
    display: flex; justify-content: center; align-items: center; gap: 30px;
  }
  .section-title h1 {
    font-family: "Roboto", Arial, sans-serif; font-weight: 700;
    font-size: 29px; letter-spacing: 2.5px; color: var(--heading);
  }
  .cards { position: absolute; left: 99px; top: 243px; display: flex; gap: 30px; }
  .card {
    width: 314px; height: 368px; background: var(--card-bg);
    border: 1px solid var(--card-border); border-top: none;
    text-align: center;
  }
  .card-photo { width: 314px; height: 215px; }
  .card-photo.dining { background: linear-gradient(160deg, #e6e0d8 0%, #cfc3b6 55%, #5a4a44 100%); }
  .card-photo.lounge { background: linear-gradient(160deg, #efe2cf 0%, #cdb69a 50%, #2e2520 100%); }
  .card-photo.living { background: linear-gradient(160deg, #d9cfc3 0%, #a88e76 50%, #6b3c28 100%); }
  .card h2 {
    margin-top: 24px;
    font-family: "Roboto", Arial, sans-serif; font-weight: 700;
    font-size: 19px; letter-spacing: 1.5px; color: var(--heading);
  }
  .card p {
    margin: 12px auto 0; width: 270px;
    font-size: 13px; line-height: 23px; color: var(--body-text);
  }

  /* Footer */
  .site-footer {
    position: absolute; left: 0; top: 664px; width: 1200px; height: 100px;
    background: var(--footer-bg); color: var(--white);
    display: flex; align-items: center; justify-content: center;
    font-size: 12.5px;
  }
  .site-footer .divider { margin: 0 9px; }
  .site-footer a { color: var(--white); text-decoration: none; }
</style>
</head>
<body>
<div class="page">
  <header class="site-header">
    <div class="brand">Velmora</div>
    <nav class="main-nav">
      <a href="#">Home</a>
      <a href="#">Building</a>
      <a href="#">Interior</a>
      <a href="#">Location</a>
    </nav>
    <a class="register-btn" href="#">REGISTER</a>
    <div class="lang-select" aria-label="Language: English">
      <svg width="25" height="16" viewBox="0 0 25 16" aria-hidden="true">
        <rect width="25" height="16" fill="#1f3a8a"/>
        <rect x="10" width="5" height="16" fill="#fff"/>
        <rect y="5.5" width="25" height="5" fill="#fff"/>
        <rect x="11" width="3" height="16" fill="#c8102e"/>
        <rect y="6.5" width="25" height="3" fill="#c8102e"/>
      </svg>
      <svg width="9" height="6" viewBox="0 0 9 6" aria-hidden="true">
        <path d="M0 0h9L4.5 6z" fill="#fff"/>
      </svg>
    </div>
  </header>

  <div class="section-title">
    <svg width="14" height="24" viewBox="0 0 14 24" aria-hidden="true">
      <path d="M12 2L3 12l9 10" fill="none" stroke="var(--chevron)" stroke-width="3"/>
    </svg>
    <h1>INTERIOR</h1>
    <svg width="14" height="24" viewBox="0 0 14 24" aria-hidden="true">
      <path d="M2 2l9 10-9 10" fill="none" stroke="var(--chevron)" stroke-width="3"/>
    </svg>
  </div>

  <section class="cards">
    <article class="card">
      <div class="card-photo dining" role="img" aria-label="Bright open-plan dining room with table, chairs and kitchen"></div>
      <h2>FINIBUS BONORUM</h2>
      <p>Sed ut perspiciatis unde omnis iste na accusantium doloremque uillo inventore verita tis et quasi archit</p>
    </article>
    <article class="card">
      <div class="card-photo lounge" role="img" aria-label="Lounge with fireplace, cream sofas and glass coffee table"></div>
      <h2>FINIBUS BONORUM</h2>
      <p>Sed ut perspiciatis unde omnis iste na accusantium doloremque uillo inventore verita tis et quasi archit</p>
    </article>
    <article class="card">
      <div class="card-photo living" role="img" aria-label="Living room with bookshelves, sofa and timber floor"></div>
      <h2>FINIBUS BONORUM</h2>
      <p>Sed ut perspiciatis unde omnis iste na accusantium doloremque uillo inventore verita tis et quasi archit</p>
    </article>
  </section>

  <footer class="site-footer">
    <span>Copyright © 2015 Velmora. All rights reserved</span>
    <span class="divider">|</span>
    <a href="#">Disclaimer</a>
  </footer>
</div>
</body>
</html>
```